Famous Swedish company need new design

This client is a family textile company since 1692 who manufactures interior textiles in Sweden, they are VURN-certified - The most heaviest and best textile certification on earth. Read more in the attached Brandbook.

They want to update their layout, a TOTAL make-over where they want to give their customers the feeling of Home & Decor but with all of their nice sales point, such as the history, swedish quality and most important: Environtment.

FOCUS ON CREATING: header, with mega menu - footer AND a product page.

Lead words: FEMININE - Modern - Nordic - Environment - History - Clean and INSPIRING

Fonts and colors - See attached Brandbook

IMPORTANT. Dont care about how the sites looks today or which content it has. Do something new and good! High-end!

Target Market(s)

Interior, design, High-end, Eco

Industry/Entity Type

Interior

Number of Pages Required

5+ page

Requirements
Must have
• Header with a mega menu for both mobile and computer.
• Product page - Inspiring and beautiful
• Footer.
Nice to have
• Product page: Image, product general info, product information full, reviews.
• Header: Cart + Wishlist, logo and menu
• Menu: mega menu, sort by Brand, product category, Collections, designers
• Footer: Something different, not only a plain color, it should feel alive somehow. Have our social medias here, newsletter and menu maybe more.
• COLORS AND FONTS - See brandbook attached

```html
<!DOCTYPE html>
<html lang="en">
<head>
<meta charset="utf-8">
<title>Hallvik — Products</title>
<link href="https://fonts.googleapis.com/css2?family=Abel&family=Oranienbaum&display=swap" rel="stylesheet">
<style>
:root{
  --ink:#1d1d1d;
  --slate:#4f6570;
  --bronze:#7a6230;
  --night:#111111;
  --paper:#ffffff;
  --scroll:#d8d8d8;
  --thumb:#555555;
}
*{box-sizing:border-box;margin:0;padding:0}
html,body{width:918px;height:1200px;overflow:hidden;background:var(--paper)}
body{position:relative;font-family:"Abel",sans-serif;color:var(--ink)}
.abs{position:absolute}

.brand{left:22px;top:6px;width:150px;text-align:center}
.brand-name{font-family:"Oranienbaum",serif;font-size:38px;line-height:40px;color:var(--ink)}
.brand-mark{display:block;margin:2px auto 0;width:18px;height:18px;border-radius:50%;background:var(--ink)}
.brand-tag{font-family:"Oranienbaum",serif;font-size:10px;letter-spacing:1px;margin-top:4px;white-space:nowrap}

.main-nav{top:28px;left:214px;display:flex;gap:29px;font-size:17px}
.social-top{top:20px;left:719px;display:flex}
.social-top span{width:28px;height:28px;border-radius:50%;background:var(--slate);margin-right:-4px;border:2px solid #fff}

.filters{top:79px;left:0;width:918px;height:22px}
.filter{position:absolute;top:0;height:20px;border:1.5px solid var(--ink);font-size:11px;padding:2px 5px;display:flex;align-items:center;justify-content:space-between;white-space:nowrap}
.filter::after,.sort::after{content:"";flex:none;width:5px;height:5px;border-right:1.5px solid var(--ink);border-bottom:1.5px solid var(--ink);transform:rotate(45deg);margin:-3px 0 0 4px}
.sort{position:absolute;left:705px;top:3px;font-size:12px;display:flex;align-items:center}
.sort::after{border-color:var(--slate)}

.page-bar{left:402px;top:116px;width:46px;height:3px;background:var(--slate)}
.page-title{left:0;width:918px;top:118px;text-align:center;font-family:"Oranienbaum",serif;font-size:35px;font-weight:bold}

.search{left:14px;top:225px;font-size:8px;display:flex;align-items:center;gap:10px}
.side-title{left:17px;font-family:"Oranienbaum",serif;font-size:17px}
.side-list{left:22px;list-style:none;font-size:9px;line-height:17.3px}
.scroll{left:96px;width:8px;background:var(--scroll)}
.scroll i{position:absolute;left:0;width:8px;background:var(--thumb)}

.card{width:160px;text-align:center}
.card .photo{display:block;margin:0 auto;width:134px;height:134px;border-radius:50%}
.card h3{font-family:"Oranienbaum",serif;font-size:11px;margin-top:12px;line-height:12px}
.card .price{font-size:12px;line-height:13px}
.card p{font-size:10px;line-height:12.7px;width:92px;margin:0 auto;text-align:left;transform:translateX(-4px)}
.swatches{display:flex;gap:9px;justify-content:center;margin-top:10px}
.swatches span{width:40px;height:19px}

.quote{left:377px;top:484px;width:164px;height:164px;border-radius:50%;background:var(--bronze);color:#fff;font-family:"Oranienbaum",serif}
.quote .open{position:absolute;left:14px;top:26px;font-size:58px;line-height:1}
.quote .big{position:absolute;left:40px;top:50px;font-size:29px;line-height:32px}
.quote .small{position:absolute;left:40px;top:86px;font-size:18px;line-height:17px}
.quote .close{position:absolute;left:112px;top:112px;font-size:58px;line-height:1}

.footer{left:0;top:995px;width:918px;height:205px;background:var(--night);color:#fff;font-family:"Oranienbaum",serif}
.fcol{position:absolute;top:16px}
.fcol h4{font-weight:normal;font-size:15px;margin-bottom:3px}
.fcol a{display:block;color:#fff;text-decoration:none;font-size:9px;line-height:23px}
.fsocial{position:absolute;left:604px;top:120px;display:flex;gap:8px}
.fsocial span{width:21px;height:21px;border:2px solid #fff;border-radius:50%}
.frule{position:absolute;left:15px;top:157px;width:903px;height:2px;background:#fff}
.copy{position:absolute;left:0;width:860px;text-align:center;top:171px;font-size:19px}
</style>
</head>
<body>

<header>
  <div class="abs brand">
    <div class="brand-name">Hallvik</div>
    <span class="brand-mark"></span>
    <div class="brand-tag">NORDIC LINEN HOUSE</div>
  </div>
  <nav class="abs main-nav"><span>Home</span><span>Our History</span><span>Designers</span><span>Brand</span><span>Collections</span><span>Products</span></nav>
  <div class="abs social-top" aria-label="Social links"><span></span><span></span><span></span></div>
  <div class="abs filters">
    <div class="filter" style="left:218px;width:50px">Size</div>
    <div class="filter" style="left:302px;width:50px">Color</div>
    <div class="filter" style="left:386px;width:49px">Fabric</div>
    <div class="filter" style="left:470px;width:82px">Design Model</div>
    <div class="filter" style="left:586px;width:50px">Price</div>
    <div class="sort">SORT BY</div>
  </div>
</header>

<div class="abs page-bar"></div>
<h1 class="abs page-title">Products</h1>

<aside>
  <div class="abs search">
    <svg width="11" height="11" viewBox="0 0 11 11"><circle cx="4.5" cy="4.5" r="3.5" fill="none" stroke="#333"/><line x1="7" y1="7" x2="10" y2="10" stroke="#333"/></svg>
    <span>Search Products..</span>
  </div>
  <h2 class="abs side-title" style="top:252px">Categories</h2>
  <ul class="abs side-list" style="top:272px">
    <li>Accessories</li><li>Baby blankets</li><li>Baby plaids</li><li>Coasters</li><li>Cushion covers</li><li>Cutting boards</li><li>Dish cloths</li><li>Plaids</li>
  </ul>
  <div class="abs scroll" style="top:277px;height:135px"><i style="top:53px;height:28px"></i></div>
  <h2 class="abs side-title" style="top:449px">Collections</h2>
  <ul class="abs side-list" style="top:469px">
    <li>Jul</li><li>Djur</li><li>Höst</li><li>Sverige</li><li>Vår</li><li>Maritimt</li><li>Mossa</li><li>Köket</li>
  </ul>
  <div class="abs scroll" style="top:473px;height:136px"><i style="top:54px;height:28px"></i></div>
</aside>

<main>
  <div class="abs card" style="left:140px;top:185px">
    <div class="photo" role="img" aria-label="Bright blue seats on a weathered stone ledge" style="background:radial-gradient(circle at 50% 40%,#1f5fd6,#c9a8a0 75%)"></div>
    <h3>Chair Ban</h3><div class="price">$900</div>
    <p>Lorem ipsum dolor sit amet, consectetur adipisicing elit, sed do eiusmod tempor incididunt ut labore et dolore magna aliqua. Ut enim ad minim veniam,</p>
    <div class="swatches"><span style="background:#4f6570"></span><span style="background:#f0682a"></span><span style="background:#85703a"></span></div>
  </div>
  <div class="abs card" style="left:393px;top:185px">
    <div class="photo" role="img" aria-label="Woven basket with patterned throw pillows" style="background:radial-gradient(circle at 50% 55%,#9a8070,#5a5a5a 75%)"></div>
    <h3>Throw Pillow</h3><div class="price">$200</div>
    <p>Lorem ipsum dolor sit amet, consectetur adipisicing elit, sed do eiusmod tempor incididunt ut labore et dolore magna aliqua. Ut enim ad minim veniam,</p>
    <div class="swatches"><span style="background:#4b0f6b"></span><span style="background:#0069c0"></span><span style="background:#11915c"></span></div>
  </div>
  <div class="abs card" style="left:646px;top:185px">
    <div class="photo" role="img" aria-label="Dining table set with bowls and a branch in a vase" style="background:radial-gradient(circle at 50% 60%,#b8b4ae,#77777a 80%)"></div>
    <h3>Dinning Set</h3><div class="price">$2900</div>
    <p>Lorem ipsum dolor sit amet, consectetur adipisicing elit, sed do eiusmod tempor incididunt ut labore et dolore magna aliqua. Ut enim ad minim veniam,</p>
    <div class="swatches"><span style="background:#7a4a22"></span><span style="background:#444444"></span><span style="background:#f7ab7c"></span></div>
  </div>

  <div class="abs quote">
    <span class="open">“</span>
    <span class="big">Bring Joy</span>
    <span class="small">To happy homes<br>each day.</span>
    <span class="close">”</span>
  </div>

  <div class="abs card" style="left:140px;top:667px">
    <div class="photo" role="img" aria-label="Wooden chair with a sheepskin and leather bag" style="background:radial-gradient(circle at 50% 45%,#7a5a45,#e8e6e2 75%)"></div>
    <h3>Champagne Chair</h3><div class="price">$8900</div>
    <p>Lorem ipsum dolor sit amet, consectetur adipisicing elit, sed do eiusmod tempor incididunt ut labore et dolore magna aliqua. Ut enim ad minim veniam,</p>
    <div class="swatches"><span style="background:#524640"></span><span style="background:#7c0000"></span><span style="background:#6fd2f5"></span></div>
  </div>
  <div class="abs card" style="left:393px;top:667px">
    <div class="photo" role="img" aria-label="Dark chair beside a yellow and black patterned textile" style="background:linear-gradient(90deg,#e8e8ea 50%,#c9b03a 50%,#2a2a2a)"></div>
    <h3>Step Chair</h3><div class="price">$5900</div>
    <p>Lorem ipsum dolor sit amet, consectetur adipisicing elit, sed do eiusmod tempor incididunt ut labore et dolore magna aliqua. Ut enim ad minim veniam,</p>
    <div class="swatches"><span style="background:#fff200"></span><span style="background:#f49ac1"></span><span style="background:#f26f4f"></span></div>
  </div>
  <div class="abs card" style="left:646px;top:667px">
    <div class="photo" role="img" aria-label="Child playing on a soft patterned blanket" style="background:radial-gradient(circle at 55% 55%,#4a3f70,#9a8a78 75%)"></div>
    <h3>Blanket</h3><div class="price">$7900</div>
    <p>Lorem ipsum dolor sit amet, consectetur adipisicing elit, sed do eiusmod tempor incididunt ut labore et dolore magna aliqua. Ut enim ad minim veniam,</p>
    <div class="swatches"><span style="background:#8c62b0"></span><span style="background:#cccccc"></span><span style="background:#ff00ee"></span></div>
  </div>
</main>

<footer class="abs footer">
  <div class="fcol" style="left:142px"><h4>ABOUT US</h4><a>About Hallvik</a><a>Copyright</a><a>Privacy Policy</a><a>Contact</a></div>
  <div class="fcol" style="left:313px"><h4>COMMUNITY</h4><a>&nbsp;</a><a>DesignForum</a><a>Book Club</a><a>Guidebooks</a></div>
  <div class="fcol" style="left:477px"><h4>Design Tips</h4><a>Start Here</a><a>DesignBlog</a><a>Destination Guides</a><a>DesignResources</a></div>
  <div class="fsocial" aria-label="Social links"><span></span><span></span><span></span></div>
  <div class="frule"></div>
  <div class="copy">Copyright © 2018 Hallvik, LLC - All rights reserved. Privacy Policy | Terms of Service</div>
</footer>

</body>
</html>
```